Strategy and Technology Consulting - Our Story and Values Page

Interior Page design – Our History and Our Values

Our homepage has been designed and we are looking for a design for one of the interior pages. This interior page tells the story of Our History and Our Values

Because the homepage has been designed, we would like this interior page to reflect the design of the homepage without being a mirror image of the homepage.

This site will be implemented in WordPress using the Elementor framework.

Font: Poppins medium and Poppins dark
Illustrations: Our homepage illustrations were designed by “Welmo 1974” on Pixaborne. Compatible original or stock illustrations are welcome. Stock photography is also welcome. Welmo is also available through Welmo Trastek on Folivane

Uploaded Files
• Homepage design – this is the design we will use for our homepage. Contest entries should reflect this basic style but should be distinctly different from the homepage.
• Our History and Our Values – Wireframe – the basic layout of the page we are looking for.
• Our History and Our Values – Word document with the text supporting the wireframe.
• Color Palette – please use colors compatible with the palette attached.

Our Story - timeline
There is a timeline element in the wireframe. The wireframe displays this as a series of chevrons (arrows), but it does not need to be. Creativity in display of the timeline is appreciated.

Our Values
If you look at the Word document, you will see that there are a lot of words on the page. The winning design will present the information in a way that engages the user without overwhelming them with too much to read. For example, they may click on a value and see more information.

Target Market(s)

CIO's and Technology Executives

Number of Pages Required

1 page

Font styles to use
Sans Serif
Other font styles liked:
• Poppin

Requirements
Must have
• A timeline element, all of our values
Nice to have
• Clever timeline display

```html
<!DOCTYPE html>
<html lang="en">
<head>
<meta charset="utf-8">
<title>Our Story and Values – Corvalis</title>
<link href="https://fonts.googleapis.com/css2?family=Barlow:wght@300;400;500;600;700&family=Poppins:wght@400;500;600;700;800&display=swap" rel="stylesheet">
<style>
:root{
  --white:#ffffff;
  --slate:#3f5570;
  --navy:#1a4e8f;
  --yellow:#f2bc1d;
  --ink:#1d1d1d;
  --body:#2c2c2c;
  --row-a:#f4f4f4;
  --row-b:#ebebeb;
  --tab:#e2e2e2;
  --bg-top:#a3b3c4;
  --bg-mid:#94a6b9;
  --footer:#4a5a73;
  --footer-deep:#3b4659;
  --muted:#dfe5ee;
}
*{margin:0;padding:0;box-sizing:border-box}
html,body{width:1200px;height:2911px;overflow:hidden}
body{position:relative;font-family:"Barlow",sans-serif;background:linear-gradient(180deg,var(--bg-top),var(--bg-mid) 60%,#8e9fb3);color:var(--body)}
.abs{position:absolute}

/* header */
.site-header{left:0;top:0;width:1200px;height:97px;background:var(--white)}
.brand{left:92px;top:22px;display:flex;align-items:center;gap:8px;font-family:"Poppins",sans-serif;font-weight:500;font-size:44px;color:#6d7a8c;line-height:54px}
.brand .dot{width:12px;height:12px;background:var(--navy);border-radius:50%}
.main-nav{left:543px;top:41px;display:flex;gap:22px;font-family:"Poppins",sans-serif;font-weight:600;font-size:13px;color:#3e4c60;align-items:center}
.main-nav span::after{content:" ⌄";font-size:11px}
.main-nav .home{width:14px;height:12px;background:#9aa6b5;clip-path:polygon(50% 0,100% 50%,85% 50%,85% 100%,15% 100%,15% 50%,0 50%)}
.btn{background:var(--yellow);color:var(--white);font-family:"Poppins",sans-serif;font-weight:700;font-size:12px;border-radius:22px;display:flex;align-items:center;justify-content:center}
.header-cta{left:980px;top:30px;width:131px;height:39px}

.section-title{left:113px;font-family:"Barlow",sans-serif;font-weight:700;font-size:30px;color:var(--slate);letter-spacing:.3px}

/* timeline */
.timeline{left:113px;top:248px;width:975px;height:306px;background:var(--white);border-radius:20px;overflow:hidden}
.tl-tabs{position:absolute;left:0;top:0;width:975px;height:60px;display:flex;gap:3px;background:var(--white)}
.tl-tabs div{background:var(--tab);font-size:25px;font-weight:400;color:var(--ink);display:flex;align-items:center;justify-content:center}
.tl-line{left:24px;top:57px;width:920px;height:7px;background:var(--navy)}
.tl-dot{top:51px;width:19px;height:19px;border-radius:50%;background:var(--yellow)}
.tl-col{top:90px;list-style:none;font-size:18px;line-height:29px;color:var(--ink)}
.tl-col li{padding-left:22px;position:relative}
.tl-col li.star::before{content:"✦";color:var(--yellow);position:absolute;left:0;font-size:15px}
.tl-col li.sub{padding-left:40px}

/* values */
.values{left:113px;top:692px;width:975px;height:1406px;border-radius:20px;overflow:hidden}
.value{position:absolute;left:0;width:975px;padding:0 38px}
.value:nth-child(odd){background:var(--row-a)}
.value:nth-child(even){background:var(--row-b)}
.value-head{display:flex;align-items:center;gap:20px;height:44px;margin-bottom:6px}
.value-icon{width:40px;height:40px;border-radius:8px;background:linear-gradient(135deg,#f2bc1d,#e86b4a 55%,#3a6fb5)}
.value h3{font-size:23px;font-weight:600;color:var(--ink)}
.value p{font-size:18px;line-height:29px;color:var(--body)}

/* footer */
.footer-wave{left:0;top:2170px;width:1200px;height:741px}
.newsletter{left:136px;top:2198px;width:926px;height:207px;background:var(--yellow);border-radius:104px}
.nl-title{left:217px;top:2250px;font-family:"Poppins",sans-serif;font-weight:800;font-size:33px;color:var(--white)}
.nl-sub{left:217px;top:2303px;font-family:"Poppins",sans-serif;font-weight:600;font-size:16px;line-height:20px;color:var(--white)}
.nl-input{left:686px;top:2280px;width:320px;height:48px;background:var(--white);border-radius:24px;display:flex;align-items:center;padding-left:22px;gap:10px;font-family:"Poppins",sans-serif;font-size:13px;color:#8b8f96}
.nl-send{position:absolute;right:5px;top:5px;width:38px;height:38px;border-radius:50%;background:#9ab0c6}

.foot-brand{left:118px;top:2585px;font-family:"Poppins",sans-serif;font-weight:500;font-size:66px;color:var(--muted);display:flex;align-items:center;gap:10px}
.foot-brand .dot{width:14px;height:14px;background:var(--white);border-radius:50%}
.socials{left:174px;top:2664px;display:flex;gap:9px}
.socials span{width:42px;height:42px;border-radius:50%;background:#6f7d93}
.foot-cta{left:213px;top:2729px;width:132px;height:38px}
.foot-col h4{font-family:"Poppins",sans-serif;font-weight:700;font-size:20px;color:var(--white);margin-bottom:18px}
.foot-col li{list-style:none;font-family:"Poppins",sans-serif;font-size:13px;color:var(--muted);height:31px}
.foot-col li::before{content:"›";margin-right:8px}
.contact-item{display:flex;gap:10px;font-family:"Poppins",sans-serif;font-size:13px;color:var(--white);line-height:18px;margin-bottom:18px}
.contact-item svg{flex:none;margin-top:2px}
.bottom-bar{left:0;top:2850px;width:1200px;height:61px;background:var(--footer-deep);display:flex;align-items:center;justify-content:center;font-family:"Poppins",sans-serif;font-weight:500;font-size:14px;color:var(--white)}
.chat{left:1136px;top:2802px;width:50px;height:50px;border-radius:50%;background:var(--yellow);display:flex;align-items:center;justify-content:center}
</style>
</head>
<body>

<header class="abs site-header">
  <div class="abs brand"><span class="dot"></span>Corvalis</div>
  <nav class="abs main-nav"><i class="home"></i><span>ABOUT US</span><span>SERVICES</span><span>INSIGHTS</span><span>JOIN US</span></nav>
  <div class="abs btn header-cta">CONTACT US</div>
</header>

<h2 class="abs section-title" style="top:168px">OUR STORY</h2>
<section class="abs timeline">
  <div class="tl-tabs">
    <div style="width:337px">2017 – 2019</div>
    <div style="width:296px">2020 – 2021</div>
    <div style="width:336px">2022 and Onward</div>
  </div>
  <div class="abs tl-line"></div>
  <div class="abs tl-dot" style="left:14px"></div>
  <div class="abs tl-dot" style="left:330px"></div>
  <div class="abs tl-dot" style="left:628px"></div>
  <div class="abs tl-dot" style="left:935px"></div>
  <ul class="abs tl-col" style="left:43px;width:240px">
    <li class="star">Growth Strategy Focus</li>
    <li class="star">Consistent, Modest Growth</li>
    <li class="star">Preliminary Focus on Technology</li>
    <li class="star">Eureka!&nbsp; Implementing strategy is hard.</li>
  </ul>
  <ul class="abs tl-col" style="left:368px;width:260px">
    <li class="star">Pandemic Pauses Growth</li>
    <li class="star">Rethinking :</li>
    <li class="sub">-&nbsp; the business model</li>
    <li class="sub">-&nbsp; the delivery model</li>
  </ul>
  <ul class="abs tl-col" style="left:702px;width:250px">
    <li class="star">Leadership Team for Focus on Essential Areas</li>
    <li class="star">Rapid Growth</li>
    <li class="star">Customer Success</li>
  </ul>
</section>

<h2 class="abs section-title" style="top:606px">OUR VALUES</h2>
<section class="abs values">
  <article class="value" style="top:0;height:197px;padding-top:30px">
    <div class="value-head"><div class="value-icon" role="img" aria-label="Icon of a hand holding a diamond"></div><h3>The Value of Every Human.&nbsp; Regardless.</h3></div>
    <p>Each person's unique experiences and perspectives add vibrant hues to the tapestry of our shared existence.&nbsp; In a world where diversity paints the canvas of humanity, true beauty is found in recognizing the inherent and incalculable value of every human being.</p>
  </article>
  <article class="value" style="top:197px;height:201px;padding-top:30px">
    <div class="value-head"><div class="value-icon" role="img" aria-label="Icon of hands joining puzzle pieces"></div><h3>Collaboration</h3></div>
    <p>Collaboration in work transforms individual endeavors into symphonies of collective achievement. Through collaboration, diverse talents converge, fostering a rich exchange of ideas that amplifies creativity, accelerates progress, and brings forth solutions beyond what a single mind could conceive.</p>
  </article>
  <article class="value" style="top:398px;height:195px;padding-top:30px">
    <div class="value-head"><div class="value-icon" role="img" aria-label="Icon of a raised fist with a check mark"></div><h3>Passion</h3></div>
    <p>Passion infuses our work with energy, transforming routine tasks into opportunities for creativity and innovation. Fueled by passion, individuals become unstoppable forces, driven to overcome challenges and achieve remarkable outcomes that benefit them and inspire those around them</p>
  </article>
  <article class="value" style="top:593px;height:201px;padding-top:30px">
    <div class="value-head"><div class="value-icon" role="img" aria-label="Icon of a person with stars and a medal"></div><h3>Excellence</h3></div>
    <p>Excellence isn't a destination; it's a continuous journey of refinement and growth. Striving for excellence cultivates a culture of continuous improvement, fostering innovation, credibility, and a lasting impact that resonates far beyond the immediate task.</p>
  </article>
  <article class="value" style="top:794px;height:201px;padding-top:36px">
    <div class="value-head"><div class="value-icon" role="img" aria-label="Icon of a clenched fist"></div><h3>Tenacity</h3></div>
    <p>Tenacity is the unwavering anchor that keeps us grounded amidst adversity, propelling us forward when faced with obstacles. The resilience to persist, adapt, and learn from setbacks leads to the mastery of skills and the fulfillment of ambitious goals</p>
  </article>
  <article class="value" style="top:995px;height:202px;padding-top:30px">
    <div class="value-head" style="margin-bottom:14px"><div class="value-icon" role="img" aria-label="Icon of a person thinking with gears"></div><h3>Solution Mindset</h3></div>
    <p>A solution mindset is the compass that directs our focus from problems to possibilities. It empowers us to navigate challenges with a proactive mindset, igniting a journey of exploration and innovation that not only resolves issues but also paves the way for continuous growth and success.</p>
  </article>
  <article class="value" style="top:1197px;height:209px;padding-top:30px">
    <div class="value-head" style="margin-bottom:14px"><div class="value-icon" role="img" aria-label="Icon of hands holding a heart"></div><h3>Generosity</h3></div>
    <p>Generosity creates a virtuous cycle of goodwill, fostering a sense of unity and shared purpose among colleagues. By freely sharing knowledge, support, and resources, we uplift those around us and contribute to a collaborative environment where collective achievements flourish.</p>
  </article>
</section>

<svg class="abs footer-wave" width="1200" height="741" viewBox="0 0 1200 741" aria-hidden="true">
  <path d="M0 50 C120 70 200 150 300 200 L900 200 C1000 120 1100 20 1200 0 L1200 741 L0 741 Z" fill="#4a5a73"/>
  <path d="M260 180 C330 290 440 290 520 230 C600 170 680 170 760 230 C840 300 920 310 980 200" fill="none" stroke="#ffffff" stroke-width="6"/>
  <path d="M250 200 C330 300 440 300 520 245 C600 190 680 190 760 245 C840 310 930 320 990 215 L990 260 L250 260 Z" fill="#4a5a73"/>
</svg>

<div class="abs newsletter"></div>
<h2 class="abs nl-title">Subscribe Our Newsletter</h2>
<p class="abs nl-sub">Subscribe our newsletter to receive the latest news<br>and exclusive offers every week, No spam.</p>
<div class="abs nl-input">
  <svg width="14" height="11" viewBox="0 0 14 11"><rect width="14" height="11" rx="1" fill="#8b8f96"/><path d="M0 1 L7 6 L14 1" stroke="#fff" fill="none"/></svg>
  Enter email address
  <span class="nl-send"><svg width="38" height="38" viewBox="0 0 38 38"><path d="M12 19 L26 12 L22 27 L19 21 Z" fill="#fff"/></svg></span>
</div>

<div class="abs foot-brand"><span class="dot"></span>Corvalis</div>
<div class="abs socials">
  <span role="img" aria-label="Social profile link"></span>
  <span role="img" aria-label="Social profile link"></span>
  <span role="img" aria-label="Video channel link"></span>
  <span role="img" aria-label="Photo profile link"></span>
</div>
<div class="abs btn foot-cta">CONTACT US</div>

<div class="abs foot-col" style="left:490px;top:2558px">
  <h4>Quick links</h4>
  <ul><li>Home</li><li>About Us</li><li>Services</li><li>Insights</li><li>Join Us</li><li>Contact Us</li></ul>
</div>
<div class="abs foot-col" style="left:668px;top:2558px">
  <h4>Our Services</h4>
  <ul><li>Business Transformation</li><li>ERP Implementations</li><li>ERP Solutions</li><li>BI and Data</li><li>Building the Right Team...</li></ul>
</div>
<div class="abs foot-col" style="left:900px;top:2558px;width:200px">
  <h4>Contact info</h4>
  <div class="contact-item"><svg width="14" height="11" viewBox="0 0 14 11"><rect width="14" height="11" rx="1" fill="#f2bc1d"/><path d="M0 1 L7 6 L14 1" stroke="#4a5a73" fill="none"/></svg><span>Email:<br>hello@corvalis-mail.com</span></div>
  <div class="contact-item"><svg width="14" height="14" viewBox="0 0 14 14"><path d="M3 1 L5 1 L6 4 L4.5 5.5 C5.5 7.5 6.5 8.5 8.5 9.5 L10 8 L13 9 L13 11 C13 12 12 13 11 13 C5.5 13 1 8.5 1 3 C1 2 2 1 3 1 Z" fill="#f2bc1d"/></svg><span>Phone:<br>+44 100 555 0142</span></div>
  <div class="contact-item"><svg width="12" height="15" viewBox="0 0 12 15"><path d="M6 0 C9.3 0 12 2.6 12 5.8 C12 10 6 15 6 15 C6 15 0 10 0 5.8 C0 2.6 2.7 0 6 0 Z" fill="#f2bc1d"/><circle cx="6" cy="5.8" r="2.2" fill="#4a5a73"/></svg><span>Location:<br>Some address line goes<br>here city name</span></div>
</div>

<div class="abs bottom-bar">© Corvalis Design 2023, All Rights Reserved</div>
<div class="abs chat"><svg width="28" height="24" viewBox="0 0 28 24"><path d="M4 2 H24 C26 2 27 3 27 5 V15 C27 17 26 18 24 18 H12 L6 23 V18 H4 C2 18 1 17 1 15 V5 C1 3 2 2 4 2 Z" fill="#fff"/><circle cx="9" cy="10" r="1.6" fill="#f2bc1d"/><circle cx="14" cy="10" r="1.6" fill="#f2bc1d"/><circle cx="19" cy="10" r="1.6" fill="#f2bc1d"/></svg></div>

</body>
</html>
```